Fitness industry business card

Dear Designers,

I'm looking to have a business card designed that will appeal to affluent wealthy clients, I would
To have high end clean cut luxurious understated minimalistic feel to the business cards.

I look forward to the first draft of design ideas. I will send the info that I would like to have on the cards shortly.

Best Wishes
Marika

```html
<!DOCTYPE html>
<html lang="en">
<head>
<meta charset="utf-8">
<title>Northline – Business Card</title>
<link rel="stylesheet" href="https://fonts.googleapis.com/css2?family=Open+Sans:wght@300;400;600;700&display=swap">
<style>
  :root {
    --page: #ffffff;
    --card-dark: #242424;
    --card-light: #d4d4d4;
    --ink-light: #ffffff;
    --ink-dark: #2a2a2a;
    --rule-light: #9a9a9a;
    --rule-dark: #6f6f6f;
    --accent-coral: #d9675a;
    --accent-aqua: #a9dcd8;
    --accent-sage: #d6e6d2;
    --card-shadow: 4px 5px 8px rgba(0,0,0,0.35);
  }
  * { box-sizing: border-box; margin: 0; padding: 0; }
  html, body {
    width: 1200px; height: 1000px; overflow: hidden;
    background: var(--page);
    font-family: "Open Sans", sans-serif;
  }
  .canvas { position: relative; width: 1200px; height: 1000px; }

  .card {
    position: absolute;
    left: 258px;
    width: 685px; height: 390px;
    background: var(--card-dark);
    box-shadow: var(--card-shadow);
    overflow: hidden;
  }
  .card--front { top: 60px; }
  .card--back { top: 530px; }

  /* Front */
  .brand-front {
    position: absolute; left: 50%; top: 50%;
    transform: translate(-50%, -50%);
    width: 210px;
  }
  .brand-front .brand-row { display: flex; align-items: center; gap: 12px; }
  .brand-mark {
    width: 12px; height: 12px; background: var(--accent-coral); flex: none;
  }
  .brand-name {
    font-weight: 600; font-size: 24px; letter-spacing: 1px; line-height: 1;
    color: var(--ink-light);
  }
  .brand-rule { height: 1px; background: var(--ink-light); margin: 8px 0 4px 24px; }
  .brand-tagline {
    margin-left: 24px;
    font-size: 11px; letter-spacing: 3px; color: var(--ink-light);
  }

  /* Back */
  .back-side {
    position: absolute; left: 0; top: 0; width: 225px; height: 100%;
    background: var(--card-light);
  }
  .brand-back { position: absolute; left: 30px; top: 300px; width: 195px; }
  .brand-back .brand-row { display: flex; align-items: center; gap: 10px; }
  .brand-back .brand-name { color: var(--ink-dark); font-size: 19px; }
  .brand-back .brand-rule { background: var(--rule-dark); margin: 7px 0 3px 22px; }
  .brand-back .brand-tagline { color: var(--ink-dark); font-size: 9.5px; letter-spacing: 2.4px; margin-left: 22px; }

  .holder { position: absolute; left: 331px; top: 100px; right: 0; }
  .holder-name {
    font-size: 21px; line-height: 1; color: var(--ink-light); font-weight: 300;
  }
  .holder-name strong { font-weight: 700; }
  .holder-rule { height: 1px; background: var(--rule-light); margin-top: 6px; }
  .holder-role {
    margin-top: 5px;
    font-size: 10px; letter-spacing: 3px; color: var(--ink-light); font-weight: 600;
  }

  .contact-list { position: absolute; left: 396px; top: 188px; list-style: none; }
  .contact-item { display: flex; align-items: center; gap: 13px; margin-bottom: 18px; }
  .contact-icon { width: 22px; height: 22px; flex: none; }
  .contact-text { font-size: 12px; line-height: 19px; color: var(--ink-light); }
</style>
</head>
<body>
<main class="canvas">

  <section class="card card--front" aria-label="Card front">
    <div class="brand-front">
      <div class="brand-row">
        <span class="brand-mark"></span>
        <span class="brand-name">NORTHLINE</span>
      </div>
      <div class="brand-rule"></div>
      <p class="brand-tagline">company provides</p>
    </div>
  </section>

  <section class="card card--back" aria-label="Card back">
    <div class="back-side">
      <div class="brand-back">
        <div class="brand-row">
          <span class="brand-mark"></span>
          <span class="brand-name">NORTHLINE</span>
        </div>
        <div class="brand-rule"></div>
        <p class="brand-tagline">company provides</p>
      </div>
    </div>

    <div class="holder">
      <h1 class="holder-name">Olesya<strong>Marika</strong></h1>
      <div class="holder-rule"></div>
      <p class="holder-role">ENGINEER</p>
    </div>

    <ul class="contact-list">
      <li class="contact-item">
        <svg class="contact-icon contact-icon--phone" viewBox="0 0 22 22" aria-hidden="true">
          <rect x="6" y="2" width="10" height="18" rx="2" fill="none" stroke="var(--accent-aqua)" stroke-width="1.6"/>
          <line x1="9.5" y1="16.5" x2="12.5" y2="16.5" stroke="var(--accent-aqua)" stroke-width="1.6"/>
        </svg>
        <p class="contact-text">+52 418 903<br>+66 512 738</p>
      </li>
      <li class="contact-item">
        <svg class="contact-icon contact-icon--mail" viewBox="0 0 22 22" aria-hidden="true">
          <rect x="2" y="5" width="18" height="12" fill="none" stroke="var(--accent-sage)" stroke-width="1.6"/>
          <polyline points="2,5 11,12 20,5" fill="none" stroke="var(--accent-sage)" stroke-width="1.6"/>
        </svg>
        <p class="contact-text">www.northlinefit.com<br>olesya@northlinefit.com</p>
      </li>
      <li class="contact-item">
        <svg class="contact-icon contact-icon--pin" viewBox="0 0 22 22" aria-hidden="true">
          <path d="M11 20 C7 14 5 11 5 8 a6 6 0 0 1 12 0 c0 3 -2 6 -6 12 z" fill="none" stroke="var(--accent-coral)" stroke-width="1.6"/>
          <circle cx="11" cy="8" r="2" fill="var(--accent-coral)"/>
        </svg>
        <p class="contact-text">41 linden row<br>Westbrook, LW 46210</p>
      </li>
    </ul>
  </section>

</main>
</body>
</html>
```